New product NuraKindle Box Packaging Design

We are looking for a product packaging design concept.

The product name is NuraKindle, Logo is attached in this post.
NuraKindle is an infant drop, with probiotic infused with Vitamin D in one. This probiotic + Vitamin D drop is for baby, and it is great for baby's digestive system, and improve immune system.
It is meant for drop per daily use.
It will be in a box, so we are looking for the box design concept.

Although it sounds like a pharmaceutical product, we want the packaging design to look more consumer-friendly, and baby-like.
North American style, modern, and baby product looking, is what we are expecting for this project. Product package needs to visually convey that it is for digestive system & it is for baby.

Some of the brands that has similar concept and products are: Velmora, K Sprigs, Harrowfield Probiotic Baby, and Quillon's Naturals. Images of the products from these brands are attached for your reference.

We are ONLY looking for the box design for now.
Feel free to contact me for any questions.

Reason: Holiday Season. Office closed. We will be ready to choose the designer in a few days. Thank you!

Target Market(s)

Baby

Industry/Entity Type

Baby

Requirements
Must have
• Our Logo, and baby like design, and visuals that indicate it is great for Baby's digestive system and immune system.

```html
<!DOCTYPE html>
<html lang="en">
<head>
<meta charset="utf-8">
<title>NuraKindle Infant Drop – Box Dieline</title>
<link href="https://fonts.googleapis.com/css2?family=Dancing+Script:wght@700&family=Open+Sans:wght@400;600;700&display=swap" rel="stylesheet">
<style>
  :root {
    --lime: #b6cf36;
    --lime-dark: #8db61c;
    --lime-deep: #6f9a12;
    --brand-green: #2bb673;
    --panel-grey: #f0f0f2;
    --die-line: #3a3a3a;
    --ink: #1f1f1f;
    --paper: #ffffff;
  }
  html, body {
    margin: 0;
    padding: 0;
    width: 1200px;
    height: 848px;
    overflow: hidden;
    background: var(--paper);
  }
  .dieline { display: block; width: 1200px; height: 848px; }
  .cut { fill: var(--paper); stroke: var(--die-line); stroke-width: 1; }
  .fold { stroke: var(--die-line); stroke-width: 1; fill: none; }
  .panel-lime { fill: var(--lime); }
  .panel-grey { fill: var(--panel-grey); }
  .panel-white { fill: var(--paper); }
  .title-arc { fill: none; stroke: var(--lime); stroke-width: 4; stroke-linecap: round; }
  .brand-name {
    font-family: "Open Sans", sans-serif;
    font-weight: 600;
    fill: var(--brand-green);
  }
  .brand-dot { fill: var(--lime); }
  .product-title {
    font-family: "Dancing Script", cursive;
    font-weight: 700;
    font-size: 45px;
    fill: var(--brand-green);
  }
  .body-text { font-family: "Open Sans", sans-serif; fill: var(--ink); }
  .body-strong { font-weight: 700; }
  .badge { fill: var(--brand-green); }
  .badge-text { font-family: "Open Sans", sans-serif; font-size: 13px; font-weight: 600; fill: var(--paper); }
  .pill { fill: var(--lime); }
  .dimension { stroke: var(--die-line); stroke-width: 1; fill: none; }
  .dimension-label { font-family: "Open Sans", sans-serif; font-size: 15px; fill: var(--ink); }
</style>
</head>
<body>
<svg class="dieline" viewBox="0 0 1200 848" xmlns="http://www.w3.org/2000/svg">
  <defs>
    <linearGradient id="photo-tone" x1="0" y1="0" x2="0" y2="1">
      <stop offset="0" stop-color="#f4f5f6"/>
      <stop offset="0.6" stop-color="#dfe6ee"/>
      <stop offset="1" stop-color="#e9ebee"/>
    </linearGradient>
    <linearGradient id="swoosh-tone" x1="0" y1="0" x2="1" y2="1">
      <stop offset="0" stop-color="#8db61c"/>
      <stop offset="1" stop-color="#b6cf36"/>
    </linearGradient>
    <clipPath id="front-clip"><rect x="220" y="224" width="288" height="359"/></clipPath>
    <clipPath id="back-clip"><rect x="652" y="224" width="288" height="359"/></clipPath>
  </defs>

  <!-- Flaps -->
  <g class="flaps">
    <path class="cut" d="M220 224 V70 Q220 44 246 44 H482 Q508 44 508 70 V224"/>
    <line class="fold" x1="220" y1="82" x2="508" y2="82"/>
    <path class="cut" d="M183 233 L220 224 V583 L183 575 Z"/>
    <path class="cut" d="M510 224 V170 Q510 158 522 158 H632 Q650 170 652 224"/>
    <path class="cut" d="M510 583 V630 Q512 648 530 648 H640 Q652 640 652 583"/>
    <path class="cut" d="M652 583 V740 Q652 762 674 762 H918 Q940 762 940 740 V583"/>
    <line class="fold" x1="652" y1="728" x2="940" y2="728"/>
    <path class="cut" d="M940 224 Q942 170 960 158 H1080 V224"/>
    <path class="cut" d="M942 583 Q944 640 956 648 H1072 Q1084 640 1084 630 V583"/>
  </g>

  <!-- Front panel -->
  <g class="front-panel" clip-path="url(#front-clip)">
    <rect class="panel-white" x="220" y="224" width="288" height="359"/>
    <path role="img" aria-label="Decorative green wave pattern" fill="url(#swoosh-tone)"
          d="M220 224 H508 V252 Q380 222 220 308 Z"/>
    <rect role="img" aria-label="Photo of a smiling baby crawling on a white blanket" x="220" y="362" width="208" height="196" fill="url(#photo-tone)"/>
    <path class="title-arc" d="M236 378 Q330 340 506 347"/>
  </g>
  <rect class="panel-lime" x="220" y="558" width="288" height="42"/>

  <g class="front-logo">
    <circle class="brand-dot" cx="367" cy="279" r="7"/>
    <text class="brand-name" x="380" y="286" font-size="19">NuraKindle</text>
  </g>
  <text class="product-title" x="374" y="336" text-anchor="middle">NuraKindle</text>
  <text class="body-text body-strong" x="480" y="361" font-size="12" text-anchor="end">Infant drop</text>
  <text class="body-text" x="480" y="373" font-size="8.5" text-anchor="end">With Probiotic infused</text>
  <text class="body-text" x="480" y="385" font-size="8.5" text-anchor="end">With Vitamin D</text>

  <rect class="badge" x="420" y="397" width="58" height="56" rx="10"/>
  <text class="badge-text" x="449" y="414" text-anchor="middle">Best</text>
  <text class="badge-text" x="449" y="431" text-anchor="middle">for</text>
  <text class="badge-text" x="449" y="448" text-anchor="middle">Baby’s</text>
  <rect class="pill" x="403" y="452" width="91" height="22" rx="11"/>
  <text class="body-text" x="448" y="467" font-size="10" text-anchor="middle">Digestive System</text>

  <text class="body-text" x="409" y="533" font-size="10">No added colors</text>
  <text class="body-text" x="409" y="548" font-size="10">or flavours</text>
  <text class="body-text" x="230" y="574" font-size="12">Content <tspan class="body-strong">8ml/ 126 Droplets</tspan></text>

  <!-- Side panel one -->
  <rect class="panel-lime" x="508" y="224" width="144" height="359"/>
  <text class="body-text" x="578" y="384" font-size="10" text-anchor="middle">Some Text here...</text>
  <text class="body-text" x="521" y="533" font-size="10">Batch No.............</text>
  <text class="body-text" x="521" y="548" font-size="10">Mfr. Date.............</text>
  <text class="body-text" x="521" y="566" font-size="10">Best before..........</text>

  <!-- Back panel -->
  <g class="back-panel" clip-path="url(#back-clip)">
    <rect class="panel-grey" x="652" y="224" width="288" height="359"/>
    <path role="img" aria-label="Decorative green wave pattern" fill="url(#swoosh-tone)"
          d="M652 484 Q760 540 940 566 V583 H652 Z"/>
  </g>
  <text class="body-text" x="795" y="357" font-size="10" text-anchor="middle">Some Text here...</text>
  <circle class="brand-dot" cx="803" cy="498" r="7"/>
  <text class="brand-name" x="816" y="505" font-size="19">NuraKindle</text>
  <text class="body-text" x="798" y="534" font-size="10">Address.....</text>

  <!-- Side panel two -->
  <rect class="panel-lime" x="940" y="224" width="144" height="359"/>
  <text class="body-text" x="1008" y="384" font-size="10" text-anchor="middle">Some Text here...</text>

  <!-- Panel outlines -->
  <g class="fold">
    <rect x="220" y="224" width="864" height="359"/>
    <line x1="508" y1="224" x2="508" y2="583"/>
    <line x1="652" y1="224" x2="652" y2="583"/>
    <line x1="940" y1="224" x2="940" y2="583"/>
  </g>

  <!-- Dimensions -->
  <g class="dimensions">
    <path class="dimension" d="M116 224 H136 M126 224 V583 M116 583 H136"/>
    <text class="dimension-label" x="152" y="411" text-anchor="middle">2.5”</text>
    <path class="dimension" d="M220 787 V807 M220 797 H652 M508 787 V807 M652 787 V807"/>
    <text class="dimension-label" x="349" y="786" text-anchor="middle">2”</text>
    <text class="dimension-label" x="576" y="786" text-anchor="middle">1”</text>
  </g>
</svg>
</body>
</html>
```